Real Estate Virtual 360 Tour Web Home Page [Design Only]

see new upload mockup attached

We want new design ideas for our home page.

Link to video from web dev team of wireframe for reference: https://files.brimvault.net/share/8qT4nLw2Xc7RzP0mVb5Kd3Hs1Jy6Ua9e/open?mode=sharing

Things desired on the home page:

Book a shoot now - Multiple markets,links to the corresponding market page for actual booking

1 Complete Package - includes Video, 3D Quellidor Tours, Exterior 360 Tours, Map, Agent Profile, Floor Plans, 2D Photos with blue sky and twilight sky guarantee

How it Works-https://clipnorra.com/581207364

Pricing-https://homewaltrip.com/pricing/

House Search-https://homewaltrip.com/

Footer
Updates

Target Market(s)

Real Estate Agents, Realtors, Home Buyers

Number of Pages Required

1 page

Font styles to use
Sans Serif

Colors
0555a3

Requirements
Must have
• see new upload mockup attached

Footer

```html
<!DOCTYPE html>
<html lang="en">
<head>
<meta charset="utf-8">
<title>Homewaltrip – Home</title>
<link href="https://fonts.googleapis.com/css2?family=Cinzel:wght@400;500&family=Roboto:ital,wght@0,400;0,500;0,700;1,400&display=swap" rel="stylesheet">
<style>
:root{
  --blue:#0a44a0;
  --blue-dark:#083a8a;
  --ink:#1d1d1d;
  --text:#666;
  --pale:#e4eefa;
  --grey:#8c8c8c;
  --grey-dark:#6f6f6f;
  --footer:#0d0d0d;
  --white:#fff;
}
*{box-sizing:border-box;margin:0;padding:0}
html,body{width:1200px;height:4736px;overflow:hidden}
body{font-family:'Roboto',sans-serif;color:var(--ink);background:var(--white);position:relative}
.serif{font-family:'Cinzel',serif;text-transform:uppercase;white-space:nowrap}
section,header,footer{position:absolute;left:0;width:1200px}
.btn{display:inline-block;font-weight:700;font-size:14px;text-transform:uppercase;text-align:center;line-height:46px;color:var(--white);background:var(--blue)}

/* header */
.site-header{top:0;height:78px;background:var(--white);border-top:3px solid var(--blue)}
.brand{position:absolute;left:145px;top:20px;display:flex;align-items:center;gap:8px;font-weight:700;font-size:22px;color:var(--blue-dark)}
.brand-dot{width:14px;height:14px;border-radius:50%;background:var(--blue)}
.nav{position:absolute;left:406px;top:0;display:flex;gap:22px;height:75px;align-items:center;font-size:11px;text-transform:uppercase;color:#333}
.nav .active{color:var(--blue);position:relative}
.nav .active::after{content:"";position:absolute;left:0;right:0;top:48px;height:3px;background:var(--blue)}
.login{position:absolute;left:966px;top:20px;width:90px;height:36px;line-height:36px;font-size:12px}

/* hero */
.hero{top:78px;height:545px;overflow:hidden}
.hero-photo{position:absolute;inset:0;background:linear-gradient(180deg,#5b8fd6 0%,#9cc0ea 35%,#7f8f6a 55%,#3f8a2e 80%,#2f6d22 100%)}
.hero-panel{position:absolute;inset:0;background:linear-gradient(160deg,#1a5cc4,#0a3f96);clip-path:polygon(78% 0,100% 0,100% 100%,45% 100%)}
.hero-panel2{position:absolute;inset:0;background:rgba(10,68,160,.75);clip-path:polygon(70% 0,78% 0,52% 100%,45% 100%)}
.hero-copy{position:absolute;left:763px;top:112px;width:420px;color:var(--white)}
.hero-copy h1{font-size:42px;font-weight:400;line-height:47px;white-space:normal}
.hero-copy p{margin-top:22px;font-size:15px;line-height:27px;width:390px}
.hero-actions{margin-top:34px;display:flex;gap:14px}
.btn-grey{background:#7f7f7f;width:155px}
.btn-outline{background:none;border:2px solid var(--white);width:155px;line-height:42px}

/* about */
.about{top:623px;height:555px}
.about-copy{position:absolute;left:145px;top:70px;width:455px}
.about-copy h2{font-size:44px;font-weight:400}
.about-copy p{margin-top:30px;font-size:12.5px;line-height:27.3px;color:var(--text)}
.about-copy .btn{margin-top:42px;width:157px}
.about-grid{position:absolute;left:657px;top:0;width:543px;height:555px;display:grid;grid-template-columns:273px 270px;grid-template-rows:278px 277px}
.tile{width:100%;height:100%}
.t1{background:linear-gradient(180deg,#9cb0c8,#8a6a55 60%,#e8eef3)}
.t2{background:linear-gradient(180deg,#b8c7d8,#5a6f8a 50%,#3b4a5e)}
.t3{background:linear-gradient(180deg,#7fa6d6,#c29060 50%,#e6e9ee)}
.t4{background:linear-gradient(180deg,#9fc2ec,#7f9bae 50%,#56707e)}

/* how it works */
.how{top:1178px;height:545px;background:var(--pale)}
.quote-card{position:absolute;left:163px;top:90px;width:354px;height:365px;background:var(--white);border-radius:22px;text-align:center;padding:52px 34px 0}
.quote-icon{display:block;margin:0 auto}
.quote-card blockquote{margin-top:18px;font-style:italic;font-size:12.3px;line-height:27px;color:#444}
.quote-card cite{display:block;margin-top:14px;font-style:normal;font-size:14px;color:var(--blue);font-weight:700}
.quote-card cite small{font-weight:400;font-style:italic;color:#666;font-size:11px}
.how-copy{position:absolute;left:580px;top:95px;width:450px}
.how-copy h2{font-size:44px;font-weight:400;margin-left:5px}
.how-copy p{margin-top:28px;font-size:12.5px;line-height:27.3px;color:var(--text)}
.how-copy p.it{margin-top:12px;font-style:italic;color:#333}
.how-copy .btn{margin-top:42px;width:157px}

/* search */
.search{top:1723px;height:284px;background:var(--grey)}
.search-intro{position:absolute;left:0;top:0;width:343px;height:284px;background:var(--blue);color:var(--white);padding:58px 0 0 55px}
.search-intro h2{font-size:44px;font-weight:400;line-height:62px}
.search-intro p{margin-top:12px;font-size:14px;font-weight:500}
.field{position:absolute;color:var(--white);font-size:12px}
.field span{display:block;margin-bottom:10px}
.input{height:40px;background:var(--white);border:1px solid #ccc;color:#555;font-size:11px;line-height:38px;padding:0 14px;position:relative}
.input.sel::after{content:"";position:absolute;right:12px;top:17px;border:4px solid transparent;border-top:5px solid #333}
.checks{position:absolute;left:373px;top:228px;font-size:12px;color:var(--white);display:flex;gap:12px}
.checks i{display:inline-block;width:9px;height:9px;border:1px solid var(--white);margin-right:5px;vertical-align:-1px}
.search-btn{position:absolute;left:580px;top:213px;width:157px}

/* listings */
.listings{top:2022px;height:313px}
.card{position:absolute;top:0;width:381px;height:313px;color:var(--white);overflow:hidden}
.card .ph{position:absolute;inset:0}
.card .tag{position:absolute;right:20px;top:20px;background:var(--blue);font-size:11px;font-weight:500;padding:0 12px;line-height:24px}
.card .price{position:absolute;left:26px;top:195px;font-size:22px;font-weight:700}
.card .addr{position:absolute;left:26px;top:240px;font-size:11px;font-weight:700}
.card .meta{position:absolute;left:26px;top:268px;font-size:9.5px;display:flex;gap:14px;align-items:center}
.card .meta b{display:inline-block;width:12px;height:8px;background:var(--white);margin-right:6px;vertical-align:-1px}
.c1 .ph{background:linear-gradient(180deg,#7d92b0,#4e6384 55%,#6b5e55)}
.c2 .ph{background:linear-gradient(180deg,#a9b9cc,#7a4d33 50%,#5b4a40)}
.c3 .ph{background:linear-gradient(180deg,#8aa5c8,#6c7786 50%,#56504a)}
.pager{position:absolute;top:2365px;left:550px;display:flex;gap:12px}
.pager span{width:42px;height:42px;border-radius:50%;border:2px solid #444;display:flex;align-items:center;justify-content:center}

/* map */
.map{top:2435px;height:535px;background:linear-gradient(135deg,#c7d6b3 0%,#e8e6dc 40%,#efece3 70%,#dfe4d4 100%)}
.map-tabs{position:absolute;left:0;top:0;display:flex;background:var(--white);font-size:15px;box-shadow:0 1px 3px rgba(0,0,0,.3)}
.map-tabs span{padding:8px 14px;color:#555}
.map-tabs span:first-child{color:#000;font-weight:500}

/* pricing */
.pricing{top:2970px;height:725px}
.pricing h2{position:absolute;top:80px;width:100%;text-align:center;font-size:44px;font-weight:400}
.plan{position:absolute;background:var(--white);box-shadow:0 4px 18px rgba(0,0,0,.12);text-align:center}
.plan .head{background:var(--grey);color:var(--white);font-size:22px}
.plan .badge{position:absolute;left:50%;transform:translateX(-50%);width:92px;height:92px;border-radius:50%;background:var(--white);border:4px solid #ddd;display:flex;align-items:center;justify-content:center;color:var(--blue);font-size:26px;font-weight:500}
.plan .badge small{font-size:13px;color:#777;font-weight:400}
.plan ul{list-style:none;text-align:left;padding-left:25px}
.plan li{font-size:13px;color:#777;line-height:31px}
.plan li::before{content:"✔";color:var(--blue);margin-right:14px;font-size:12px}
.plan .more{position:absolute;left:20px;right:20px;border-top:1px solid #eee;color:var(--blue);font-size:14px;font-weight:500}
.p1{left:197px;top:225px;width:252px;height:390px}
.p3{left:752px;top:225px;width:252px;height:390px}
.p1 .head,.p3 .head{height:118px;padding-top:22px}
.p1 .badge,.p3 .badge{top:72px}
.p1 ul,.p3 ul{margin-top:85px}
.p1 .more,.p3 .more{top:328px;padding-top:20px}
.p2{left:448px;top:195px;width:304px;height:440px;z-index:2}
.p2 .head{background:var(--blue);height:130px;padding-top:28px;font-size:23px}
.p2 .badge{top:82px;width:100px;height:100px}
.p2 ul{margin-top:92px;padding-left:60px}
.p2 li{font-size:15px;line-height:36px}
.p2 .more{top:372px;padding-top:20px;font-size:16px}

/* team */
.team{top:3695px;height:667px;background:var(--blue);color:var(--white);text-align:center}
.team h2{position:absolute;top:58px;width:100%;font-size:44px;font-weight:400}
.member{position:absolute;top:165px;width:250px}
.member .frame{width:240px;height:240px;margin:0 auto;border-radius:50%;background:var(--white);padding:22px;position:relative}
.member .portrait{width:100%;height:100%;border-radius:50%;background:linear-gradient(180deg,#e9edf1,#b9c2cc 60%,#4d5d78)}
.member .link{position:absolute;left:50%;bottom:-14px;transform:translateX(-50%);width:34px;height:34px;border-radius:50%;background:#555}
.member h3{margin-top:32px;font-size:20px;font-weight:400}
.member p{margin-top:14px;font-size:14px;line-height:24px}
.m1{left:140px}.m2{left:476px}.m3{left:812px}
.team .btn{position:absolute;left:523px;top:542px;width:155px;background:var(--grey)}

/* footer */
.site-footer{top:4362px;height:328px;background:var(--footer);color:var(--white)}
.col{position:absolute;top:65px}
.col h4{font-size:19px;font-weight:400;text-transform:uppercase;margin-bottom:18px}
.col ul{list-style:none;font-size:10.5px;line-height:18px}
.contact li{display:flex;gap:18px;margin-bottom:14px;font-size:10.5px;line-height:13px}
.contact svg{flex:none}
.socials{display:flex;gap:10px;margin-top:6px}
.socials span{width:32px;height:32px;border:2px solid var(--white);border-radius:50%}
.newsletter p{font-size:10.5px}
.newsletter .email{margin-top:18px;width:234px;height:34px;background:var(--white);color:#555;font-size:10px;line-height:34px;padding-left:12px}
.newsletter .btn{margin-top:10px;width:100px;height:32px;line-height:32px;font-size:11px;font-weight:500}
.copyright{top:4690px;height:46px;background:var(--footer);border-top:1px solid #333;color:var(--white);font-size:10.5px;text-align:center;line-height:44px}
</style>
</head>
<body>

<header class="site-header">
  <div class="brand"><span class="brand-dot"></span>Homewaltrip</div>
  <nav class="nav">
    <span class="active">Houses</span><span>Land</span><span>Commercial</span><span>Pricing</span><span>Career Opportunities</span><span>Covid-19 Protocols</span>
  </nav>
  <span class="btn login">Login</span>
</header>

<section class="hero">
  <div class="hero-photo" role="img" aria-label="Ranch style home with green lawn and mountain views under a blue sky"></div>
  <div class="hero-panel2"></div>
  <div class="hero-panel"></div>
  <div class="hero-copy">
    <h1 class="serif">4810 Aspen Ridge<br>Way Marlow<br>Creek,<br>CO 80190</h1>
    <p>Welcome To The Jaw-Dropping Mountain Views In This Ranch Style Home on a 1/2 Acre...</p>
    <div class="hero-actions"><span class="btn btn-grey">Get Started</span><span class="btn btn-outline">Read More</span></div>
  </div>
</section>

<section class="about">
  <div class="about-copy">
    <h2 class="serif">About Us</h2>
    <p>Welcome To The Jaw-Dropping Mountain Views In This Ranch Style Home on a 1/2 Acre Lot In Sablebrook! Upon Entering You Are Greeted By Flowing Engineered Hardwood Floors. Enjoy Cozying Up On Cold Colorado Nights In This Stunning Family Room Next To The 3 Sided Fireplace With Stacked Stone And Custom Live Edge Mantel. This Kitchen Is Perfect For The Chef In Your Family With Double Ovens, Stainless Steel Appliances, Quartz Counters, Tile Brick Backsplash, Newer Pendant Lights, Bar Eating Space, And Breakfast Nook. The Dining Room Is Sure To Impress With A Hearthline Light Fixture, Crown Molding, And Engineered Hardwood Floors.</p>
    <span class="btn">Read More</span>
  </div>
  <div class="about-grid">
    <div class="tile t1" role="img" aria-label="Brick house with porch in winter"></div>
    <div class="tile t2" role="img" aria-label="Victorian style painted house"></div>
    <div class="tile t3" role="img" aria-label="Two storey home with garage in snow"></div>
    <div class="tile t4" role="img" aria-label="Downtown glass residential tower"></div>
  </div>
</section>

<section class="how">
  <div class="quote-card">
    <svg class="quote-icon" width="60" height="58" viewBox="0 0 60 58" aria-hidden="true"><path d="M30 4a25 23 0 1 0 0 46c3 0 6-.5 9-1.5L50 54l-3-11a22 22 0 0 0 8-16A25 23 0 0 0 30 4z" fill="none" stroke="#0a44a0" stroke-width="3.5"/><text x="30" y="38" text-anchor="middle" font-family="Georgia,serif" font-size="30" font-weight="700" fill="#0a44a0">”</text></svg>
    <blockquote>"Duis aute irure dolor in reprehenderit in voluptate velit esse cillum dolore eu fugiat nulla pariatur. xcepteur sint occaecat cupidatat non proident sunt in culpa qui officia deserunt mollit anim id estaccusantium doloremq laborum"</blockquote>
    <cite>- SAM CARVER,<small>Customer</small></cite>
  </div>
  <div class="how-copy">
    <h2 class="serif">How It Works</h2>
    <p>Lorem ipsum dolor sit amet, consectetur adipiscing elit, sed do eiusmod tempor incididunt ut labore et dolore magna aliqua. Ut enim ad minim veniam, quis nostrud exercitation ullamco laboris nisi ut aliquip</p>
    <p class="it">"Duis aute irure dolor in reprehenderit in voluptate velit esse cillum dolore eu fugiat nulla pariatur. Excepteur sint occaecat cupidatat non proident, sunt in culpa qui officia deserunt mollit anim id est laborum"</p>
    <span class="btn">Read More</span>
  </div>
</section>

<section class="search">
  <div class="search-intro"><h2 class="serif">Search<br>Houses</h2><p>USE FILTERS</p></div>
  <div class="field" style="left:373px;top:20px;width:297px"><span>Cities</span><div class="input sel">Select city</div></div>
  <div class="field" style="left:689px;top:20px;width:129px"><span>Price Min</span><div class="input sel">Select city</div></div>
  <div class="field" style="left:828px;top:20px;width:129px"><span>Price Max</span><div class="input sel">Select city</div></div>
  <div class="field" style="left:968px;top:20px;width:87px"><span>Min Bedrooms</span><div class="input sel">1</div></div>
  <div class="field" style="left:1065px;top:20px;width:88px"><span>Min Bathrooms</span><div class="input sel">1</div></div>
  <div class="field" style="left:373px;top:122px;width:297px"><span>Property types</span><div class="input sel">Select city</div></div>
  <div class="field" style="left:689px;top:122px;width:129px"><span>Show houses within</span><div class="input">20</div></div>
  <div class="field" style="left:828px;top:122px;width:129px"><span>Price Max</span><div class="input sel">mi</div></div>
  <div class="field" style="left:968px;top:122px;width:185px"><span>Enter location</span><div class="input">1</div></div>
  <div class="checks"><span><i></i>Garage</span><span><i></i>Basement</span></div>
  <span class="btn search-btn">Search</span>
</section>

<section class="listings">
  <article class="card c1" style="left:14px">
    <div class="ph" role="img" aria-label="Blue two storey house"></div>
    <span class="tag">FOR SALE</span><div class="price">$310000</div>
    <div class="addr">1207 BRINDLE ST UNIT B HARLOW, CO 80155</div>
    <div class="meta"><span><b></b>BEDS</span><span><b></b>2 BATHS: 2</span><span><b></b>1304 FT2</span></div>
  </article>
  <article class="card c2" style="left:410px">
    <div class="ph" role="img" aria-label="Wooden cabin in snow"></div>
    <span class="tag">FOR SALE</span><div class="price">$310000</div>
    <div class="addr">9420 TIMBER BEND RD PINECREST, CO 80467</div>
    <div class="meta"><span><b></b>BEDS</span><span><b></b>2 BATHS: 2</span><span><b></b>1304 FT2</span></div>
  </article>
  <article class="card c3" style="left:805px">
    <div class="ph" role="img" aria-label="Single storey house with covered porch"></div>
    <span class="tag">FOR SALE</span><div class="price">$295000</div>
    <div class="addr">3305 ORCHID LN DALEWOOD, CO 80038</div>
    <div class="meta"><span><b></b>BEDS</span><span><b></b>2 BATHS: 2</span><span><b></b>1304 FT2</span></div>
  </article>
</section>
<div class="pager">
  <span><svg width="12" height="16" viewBox="0 0 12 16"><path d="M9 2L3 8l6 6" fill="none" stroke="#333" stroke-width="2"/></svg></span>
  <span><svg width="12" height="16" viewBox="0 0 12 16"><path d="M3 2l6 6-6 6" fill="none" stroke="#333" stroke-width="2"/></svg></span>
</div>

<section class="map" role="img" aria-label="Road map of the Front Range region with listing markers">
  <div class="map-tabs"><span>Map</span><span>Satellite</span></div>
</section>

<section class="pricing">
  <h2 class="serif">Pricing Plan</h2>
  <div class="plan p1">
    <div class="head">Plan 1</div><div class="badge">$10<small>/mo</small></div>
    <ul><li>Iusto odio dignissimos</li><li>Voluptatum deleniti</li><li>Omnis dolor repellendus</li><li>Repudiandae sint</li></ul>
    <div class="more">View Details »</div>
  </div>
  <div class="plan p2">
    <div class="head">Plan 2</div><div class="badge">$20<small>/mo</small></div>
    <ul><li>Iusto odio dignissimos</li><li>Voluptatum deleniti</li><li>Omnis dolor repellendus</li><li>Repudiandae sint</li></ul>
    <div class="more">View Details »</div>
  </div>
  <div class="plan p3">
    <div class="head">Plan 3</div><div class="badge">$30<small>/mo</small></div>
    <ul><li>Iusto odio dignissimos</li><li>Voluptatum deleniti</li><li>Omnis dolor repellendus</li><li>Repudiandae sint</li></ul>
    <div class="more">View Details »</div>
  </div>
</section>

<section class="team">
  <h2 class="serif">Our Team</h2>
  <div class="member m1"><div class="frame"><div class="portrait" role="img" aria-label="Portrait of team member Tomas Reyl"></div><span class="link"></span></div><h3>TOMAS REYL</h3><p>Sed ut perspiciatis unmnis<br>iste natus</p></div>
  <div class="member m2"><div class="frame"><div class="portrait" role="img" aria-label="Portrait of team member Lena Vorst"></div><span class="link"></span></div><h3>LENA VORST</h3><p>Sed ut perspiciatis unmnis<br>iste natus</p></div>
  <div class="member m3"><div class="frame"><div class="portrait" role="img" aria-label="Portrait of team member Evan Holt"></div><span class="link"></span></div><h3>EVAN HOLT</h3><p>Sed ut perspiciatis unmnis<br>iste natus</p></div>
  <span class="btn">View More</span>
</section>

<footer class="site-footer">
  <div class="col contact" style="left:145px;width:260px">
    <h4>Contact Us</h4>
    <ul>
      <li><svg width="10" height="14" viewBox="0 0 10 14"><path d="M5 0a5 5 0 0 0-5 5c0 4 5 9 5 9s5-5 5-9a5 5 0 0 0-5-5zm0 7a2 2 0 1 1 0-4 2 2 0 0 1 0 4z" fill="#fff"/></svg>Address: 57 Marrow Ave<br>Elmbrook, CO 80519</li>
      <li><svg width="13" height="13" viewBox="0 0 13 13"><path d="M3 0l2 3-1.5 1.5a8 8 0 0 0 5 5L10 8l3 2-1 3C6 13 0 7 0 1z" fill="#fff"/></svg>Call or Text Us at: 555-014-2290</li>
      <li><svg width="13" height="10" viewBox="0 0 13 10"><rect width="13" height="10" fill="#fff"/><path d="M0 0l6.5 5L13 0" fill="none" stroke="#0d0d0d"/></svg>Email Direct at: hello@homewaltrip.com</li>
    </ul>
    <div class="socials" aria-label="Social links"><span></span><span></span><span></span><span></span></div>
  </div>
  <div class="col" style="left:438px"><h4>Quick Links</h4><ul><li>Houses</li><li>Land</li><li>Commercial</li><li>Pricing</li><li>Career Opportunities</li><li>Contact</li><li>COVID-19 Protocols</li></ul></div>
  <div class="col" style="left:610px"><h4>Other Links</h4><ul><li>FAQ</li><li>Support</li><li>Sitemap</li><li>Terms Of Use</li><li>Privacy Statement</li></ul></div>
  <div class="col newsletter" style="left:814px"><h4>Sign Up Newsletter</h4><p>Sed ut perspiciatis unde omnis iste natus error</p><div class="email">Enter Email</div><span class="btn">Sign Up</span></div>
</footer>
<div class="copyright" style="position:absolute;left:0;width:1200px">© copyright 2020 Homewaltrip All Rights Reserved | Privacy Policy | Terms and use</div>

</body>
</html>
```